"Willow Drift" Mattress Pad Packaging

We need packaging for a mattress pad. This will be sold through retailers across North America. We need something modern and clean, an update from what we currently have. This is targeted towards older women. I've attached what our current packaging looks like as well as other mattress pad packaging. This is a simple product so we're open to creativity and experimentation. This is our first time using this site so we're very open and hoping for something fun.

Font styles to use
Serif
Sans Serif

Colors

Designer to choose colors to be used in the design.

```html
<!DOCTYPE html>
<html lang="en">
<head>
<meta charset="utf-8">
<title>Willow Drift Mattress Pad Packaging</title>
<link href="https://fonts.googleapis.com/css2?family=Cinzel:wght@400;600;700&family=Cormorant+SC:wght@400;500;700&display=swap" rel="stylesheet">
<style>
  :root {
    --gold-dark: #b8893d;
    --gold-mid: #c9a25a;
    --gold-light: #dcbb7a;
    --paper: #ffffff;
    --ink: #000000;
    --quilt-light: #f4f4f4;
    --quilt-shade: #d9d9d9;
  }
  * { margin: 0; padding: 0; box-sizing: border-box; }
  html, body { width: 1200px; height: 669px; overflow: hidden; background: var(--paper); }
  .canvas { position: relative; width: 1200px; height: 669px; display: flex; }

  .panel { position: relative; width: 600px; height: 669px; }
  .panel--light { background: var(--paper); }
  .panel--dark { background: var(--ink); }

  .frame {
    position: absolute; left: 21px; top: 21px; width: 558px; height: 627px;
    border: 9px solid var(--gold-mid);
    border-image: linear-gradient(90deg, var(--gold-dark), var(--gold-light), var(--gold-dark)) 1;
  }

  .quilt {
    position: absolute; left: 30px; top: 30px; width: 540px; height: 200px;
  }

  .line {
    position: absolute; left: 0; width: 600px; text-align: center;
    font-family: "Cinzel", serif; color: var(--gold-mid);
    background: linear-gradient(90deg, var(--gold-dark), var(--gold-light) 55%, var(--gold-dark));
    -webkit-background-clip: text; background-clip: text; -webkit-text-fill-color: transparent;
    white-space: nowrap; line-height: 1;
  }
  .brand-name { top: 160px; font-size: 27px; letter-spacing: 2.5px; }
  .brand-line { top: 193px; font-size: 11px; letter-spacing: 4.2px; }
  .title-main { top: 255px; font-size: 78px; letter-spacing: 1px; }
  .title-sub { top: 330px; font-size: 19px; letter-spacing: 18.5px; padding-left: 18px; }
  .title-end { top: 356px; font-size: 78px; letter-spacing: 2px; }
  .spec { font-family: "Cormorant SC", serif; font-size: 17px; letter-spacing: 0.3px; }
  .spec--1 { top: 445px; }
  .spec--2 { top: 465px; }
  .spec--3 { top: 485px; }
  .size { top: 524px; font-family: "Cormorant SC", serif; font-weight: 700; font-size: 17px; }

  .features { position: absolute; left: 0; top: 564px; width: 600px; }
  .feature { position: absolute; width: 100px; margin-left: -50px; text-align: center; }
  .feature--water { left: 179px; }
  .feature--air { left: 307px; }
  .feature--cotton { left: 435px; }
  .feature svg { display: block; margin: 0 auto; width: 46px; height: 42px; }
  .feature-label {
    margin-top: 8px; font-family: "Cormorant SC", serif; font-size: 11.5px; letter-spacing: 0.3px;
    color: var(--gold-mid);
  }
</style>
</head>
<body>
<main class="canvas">

  <section class="panel panel--light" aria-label="Light packaging variant">
    <svg class="quilt" viewBox="0 0 540 200" role="img" aria-label="Photo of a white quilted mattress pad">
      <defs>
        <linearGradient id="quiltLight" x1="0" y1="0" x2="0" y2="1">
          <stop offset="0" stop-color="#ffffff"/>
          <stop offset="0.35" stop-color="#f3f3f3"/>
          <stop offset="1" stop-color="#dedede"/>
        </linearGradient>
      </defs>
      <path d="M0 110 Q120 80 270 82 Q420 84 540 100 V190 Q510 200 480 192 Q450 184 420 194 Q390 202 360 192 Q330 184 300 194 Q270 202 240 192 Q210 184 180 194 Q150 202 120 192 Q90 184 60 194 Q30 202 0 192 Z" fill="url(#quiltLight)"/>
    </svg>
    <div class="frame"></div>
    <p class="line brand-name">WILLOW DRIFT</p>
    <p class="line brand-line">HOME COLLECTION</p>
    <h1 class="line title-main">MATTRESS</h1>
    <p class="line title-sub">LUXURY QUILTED</p>
    <p class="line title-end">PAD</p>
    <p class="line spec spec--1">300 Thread Count</p>
    <p class="line spec spec--2">Stretch-to-Fit-Skirt &nbsp;|&nbsp; Allergy Deterrent</p>
    <p class="line spec spec--3">100% Cotton</p>
    <p class="line size">Queen</p>
    <div class="features">
      <div class="feature feature--water">
        <svg viewBox="0 0 46 42"><path d="M23 2 C17 14 11 21 11 29 A12 12 0 0 0 35 29 C35 21 29 14 23 2 Z" fill="none" stroke="#c9a25a" stroke-width="2.5"/><path d="M17 28 A7 7 0 0 0 25 36" fill="none" stroke="#c9a25a" stroke-width="3"/></svg>
        <p class="feature-label">WATERPROOF</p>
      </div>
      <div class="feature feature--air">
        <svg viewBox="0 0 46 42"><path d="M17 4 V30 M11 26 L17 38 L23 26 Z" fill="#c9a25a" stroke="#c9a25a" stroke-width="3"/><path d="M29 38 V12 M23 16 L29 4 L35 16 Z" fill="#c9a25a" stroke="#c9a25a" stroke-width="3"/></svg>
        <p class="feature-label">BREATHABLE</p>
      </div>
      <div class="feature feature--cotton">
        <svg viewBox="0 0 46 42"><path d="M10 32 A8 8 0 0 1 8 17 A9 9 0 0 1 17 9 A10 10 0 0 1 34 10 A9 9 0 0 1 40 22 A7 7 0 0 1 36 32 Z" fill="none" stroke="#c9a25a" stroke-width="2.5"/><path d="M15 32 Q23 24 31 32 M23 32 L23 24" fill="none" stroke="#c9a25a" stroke-width="2"/></svg>
        <p class="feature-label">COTTON</p>
      </div>
    </div>
  </section>

  <section class="panel panel--dark" aria-label="Dark packaging variant">
    <svg class="quilt" viewBox="0 0 540 200" role="img" aria-label="Photo of a white quilted mattress pad">
      <defs>
        <linearGradient id="quiltDark" x1="0" y1="0" x2="0" y2="1">
          <stop offset="0" stop-color="#ffffff"/>
          <stop offset="0.5" stop-color="#eeeeee"/>
          <stop offset="1" stop-color="#d6d6d6"/>
        </linearGradient>
      </defs>
      <path d="M0 0 H540 V190 Q510 200 480 192 Q450 184 420 194 Q390 202 360 192 Q330 184 300 194 Q270 202 240 192 Q210 184 180 194 Q150 202 120 192 Q90 184 60 194 Q30 202 0 192 Z" fill="url(#quiltDark)"/>
    </svg>
    <div class="frame"></div>
    <p class="line brand-name">WILLOW DRIFT</p>
    <p class="line brand-line">HOME COLLECTION</p>
    <h2 class="line title-main">MATTRESS</h2>
    <p class="line title-sub">LUXURY QUILTED</p>
    <p class="line title-end">PAD</p>
    <p class="line spec spec--1">300 Thread Count</p>
    <p class="line spec spec--2">Stretch-to-Fit-Skirt &nbsp;|&nbsp; Allergy Deterrent</p>
    <p class="line spec spec--3">100% Cotton</p>
    <p class="line size">Queen</p>
    <div class="features">
      <div class="feature feature--water">
        <svg viewBox="0 0 46 42"><path d="M23 2 C17 14 11 21 11 29 A12 12 0 0 0 35 29 C35 21 29 14 23 2 Z" fill="none" stroke="#c9a25a" stroke-width="2.5"/><path d="M17 28 A7 7 0 0 0 25 36" fill="none" stroke="#c9a25a" stroke-width="3"/></svg>
        <p class="feature-label">WATERPROOF</p>
      </div>
      <div class="feature feature--air">
        <svg viewBox="0 0 46 42"><path d="M17 4 V30 M11 26 L17 38 L23 26 Z" fill="#c9a25a" stroke="#c9a25a" stroke-width="3"/><path d="M29 38 V12 M23 16 L29 4 L35 16 Z" fill="#c9a25a" stroke="#c9a25a" stroke-width="3"/></svg>
        <p class="feature-label">BREATHABLE</p>
      </div>
      <div class="feature feature--cotton">
        <svg viewBox="0 0 46 42"><path d="M10 32 A8 8 0 0 1 8 17 A9 9 0 0 1 17 9 A10 10 0 0 1 34 10 A9 9 0 0 1 40 22 A7 7 0 0 1 36 32 Z" fill="none" stroke="#c9a25a" stroke-width="2.5"/><path d="M15 32 Q23 24 31 32 M23 32 L23 24" fill="none" stroke="#c9a25a" stroke-width="2"/></svg>
        <p class="feature-label">COTTON</p>
      </div>
    </div>
  </section>

</main>
</body>
</html>
```